Oven Cleaning Business owner needs business card design

Hi there,
Would like for a business card to be designed for myself, the owner of a professional oven cleaning business on the Sunshine Coast.
Would like it to look sleek, and modern-ish. Bit creative is encouraged too.
Include following:
Name/title: Corin de Walbrek, Owner
Phone number: 1300 482 906
Email: info@kitchenlustrely.com.au
Website: www.kitchenlustrely.com.au

```html
<!DOCTYPE html>
<html lang="en">
<head>
<meta charset="UTF-8">
<title>Kitchen Lustrely – Business Card</title>
<link href="https://fonts.googleapis.com/css2?family=Montserrat:wght@500;700&family=Roboto:wght@400&display=swap" rel="stylesheet">
<style>
  :root {
    --bg: #3a3a3a;
    --card: #131313;
    --teal: #4ec3c9;
    --white: #f2f2f2;
    --grey: #b9b9b9;
  }
  * { margin: 0; padding: 0; box-sizing: border-box; }
  html, body {
    width: 1200px; height: 801px; overflow: hidden;
    background: var(--bg);
  }
  .stage {
    width: 1200px; height: 801px;
    display: flex; align-items: center; justify-content: center; gap: 50px;
  }
  .card {
    width: 525px; height: 300px;
    background: var(--card);
    border-bottom: 3px solid var(--teal);
    position: relative;
    box-shadow: 0 14px 30px rgba(0,0,0,0.35);
  }
  /* Contact side */
  .contact-side {
    display: flex; align-items: center; justify-content: center;
  }
  .identity {
    text-align: right; padding-right: 16px;
    border-right: 1.5px solid var(--teal);
    padding-top: 4px; padding-bottom: 4px;
  }
  .identity .name {
    font-family: 'Montserrat', sans-serif; font-weight: 700;
    font-size: 19px; color: var(--teal); text-transform: uppercase;
    letter-spacing: 0.2px;
  }
  .identity .title {
    font-family: 'Roboto', sans-serif; font-size: 13px; color: var(--grey);
    margin-top: 2px;
  }
  .details { list-style: none; padding-left: 14px; }
  .details li {
    display: flex; align-items: center; gap: 7px;
    font-family: 'Roboto', sans-serif; font-size: 12.5px; color: var(--white);
    line-height: 19px;
  }
  .details svg { width: 10px; height: 10px; flex: none; }
  /* Brand side */
  .brand-side {
    display: flex; align-items: center; justify-content: center; gap: 14px;
  }
  .brand-dot {
    width: 40px; height: 40px; border-radius: 50%; background: var(--teal);
  }
  .brand-name {
    font-family: 'Montserrat', sans-serif; font-weight: 700;
    font-size: 38px; color: var(--teal); text-transform: uppercase;
    letter-spacing: 1px;
  }
</style>
</head>
<body>
<main class="stage">
  <section class="card contact-side">
    <div class="identity">
      <p class="name">Corin de Walbrek</p>
      <p class="title">Owner</p>
    </div>
    <ul class="details">
      <li>
        <svg viewBox="0 0 10 10" aria-hidden="true"><path fill="#4ec3c9" d="M2 0.5 L3.6 2.6 L2.8 3.6 Q3.8 5.9 6.4 7.2 L7.4 6.4 L9.5 8 L8.3 9.5 Q2.5 8.6 0.5 1.7 Z"/></svg>
        1300 482 906
      </li>
      <li>
        <svg viewBox="0 0 10 10" aria-hidden="true"><rect x="0.5" y="2" width="9" height="6.5" fill="#4ec3c9"/><path d="M0.8 2.3 L5 5.6 L9.2 2.3" stroke="#131313" stroke-width="1" fill="none"/></svg>
        info@kitchenlustrely.com.au
      </li>
      <li>
        <svg viewBox="0 0 10 10" aria-hidden="true"><circle cx="5" cy="5" r="4.3" fill="none" stroke="#4ec3c9" stroke-width="1.2"/><ellipse cx="5" cy="5" rx="1.8" ry="4.3" fill="none" stroke="#4ec3c9" stroke-width="1"/><line x1="0.7" y1="5" x2="9.3" y2="5" stroke="#4ec3c9" stroke-width="1"/></svg>
        www.kitchenlustrely.com.au
      </li>
    </ul>
  </section>
  <section class="card brand-side">
    <span class="brand-dot" aria-hidden="true"></span>
    <span class="brand-name">Kitchen Lustrely</span>
  </section>
</main>
</body>
</html>
```